Lumora Flow Collective Business Cards

I need business cards for staff in a new startup. Our company name is MorvaLeap - we train Tai Chi teachers. But our biggest project is called Lumora Flow Collective - a federal project to put together free Tai Chi classes for Vets all across America. It's a young company, with a spirit of excitement, passion, a desire to do good for others (our Vets) and a modern style and sensibility. In other words, not old-fashioned Asian martial arts theme, but something new.

Industry/Entity Type

Health And Wellness

Contact Information for Business Card

The topic is ancient healing, but the company is the Quibbletons - so I'd like a card design that captures that.

Font styles to use
Sans Serif

Colors

Designer to choose colors to be used in the design.

Requirements
Nice to have
• I've got two logos - one for the company and one for the project. I want to see if we can incorporate them both without it becoming too busy.
Should not have
• Overly old-fashioned yin-yang themes.

```html
<!DOCTYPE html>
<html lang="en">
<head>
<meta charset="utf-8">
<title>Lumora Flow Collective Business Cards</title>
<link rel="stylesheet" href="https://fonts.googleapis.com/css2?family=PT+Sans:wght@400&display=swap">
<style>
  :root {
    --bg: #f4f5f5;
    --navy: #2b2e5f;
    --tagline: #474b7d;
    --white: #ffffff;
    --ink: #2b2e5f;
    --muted: #d6d6d6;
    --red: #e3262b;
  }
  html, body {
    margin: 0;
    width: 1200px;
    height: 1200px;
    overflow: hidden;
    background: var(--bg);
    font-family: "PT Sans", "Myriad Pro", Arial, sans-serif;
  }
  .card {
    position: absolute;
    top: 276px;
    width: 359px;
    height: 629px;
    box-sizing: border-box;
  }
  .card--front { left: 198px; background: var(--navy); }
  .card--back  { left: 632px; background: var(--white); box-shadow: 0 0 0 1px #e6e6e6; }

  .project-mark {
    position: absolute;
    left: 0; right: 0;
    top: 290px;
    display: flex;
    align-items: center;
    justify-content: center;
    gap: 12px;
  }
  .project-mark__dot {
    width: 34px; height: 34px;
    border: 2px solid var(--white);
    border-radius: 50%;
    box-sizing: border-box;
  }
  .project-mark__name {
    color: var(--white);
    font-size: 21px;
    letter-spacing: 0.5px;
  }
  .tagline {
    position: absolute;
    left: 0; right: 0;
    top: 565px;
    text-align: center;
    color: var(--tagline);
    font-size: 19px;
    letter-spacing: 7px;
  }

  .contact {
    position: absolute;
    left: 65px;
    top: 243px;
    color: var(--ink);
  }
  .contact__address { font-size: 19px; line-height: 24.5px; margin: 0; }
  .contact__phone { font-size: 15px; margin: 26px 0 0; line-height: 20px; }
  .contact__email { font-size: 19px; margin: 0; line-height: 22px; }

  .parent-brand {
    position: absolute;
    right: 30px;
    top: 492px;
    text-align: right;
  }
  .parent-brand__label { color: var(--muted); font-size: 14px; margin: 0 0 14px; }
  .parent-brand__mark { display: flex; align-items: center; justify-content: flex-end; gap: 8px; }
  .parent-brand__dot { width: 30px; height: 30px; border-radius: 50%; background: var(--red); }
  .parent-brand__name { color: var(--red); font-size: 20px; }
</style>
</head>
<body>
  <section class="card card--front">
    <div class="project-mark">
      <span class="project-mark__dot"></span>
      <span class="project-mark__name">Lumora Flow Collective</span>
    </div>
    <p class="tagline">mind · body · soul</p>
  </section>

  <section class="card card--back">
    <div class="contact">
      <p class="contact__address">Elias Marrow<br>1874 Cedar Hollow Lane<br>Brookfield TN, 38022</p>
      <p class="contact__phone">555-014-2278</p>
      <p class="contact__email">elias.marrow@morvaleap.com</p>
    </div>
    <div class="parent-brand">
      <p class="parent-brand__label">an initiative by</p>
      <div class="parent-brand__mark">
        <span class="parent-brand__dot"></span>
        <span class="parent-brand__name">MorvaLeap</span>
      </div>
    </div>
  </section>
</body>
</html>
```